New Business Card for Web Design/Internet Marketing Company

Looking for a great looking new business card. We are a 10 year old web design, internet marketing and website management company that works mostly with small businesses.

Our new card needs to better match the colors and style of our website, be bold, extremely usable and slightly edgy.

Target Market(s)

Small/Medium businesses that have websites

Industry/Entity Type

Internet

Requirements
Must have
• Front and back design, full color, rounded corners please

Must use the colors/style of our website (JPG provided)

INFO FOR CARDS (as readable as possible please)
Mark Pellow
President/CEO
mark@brightlanesites.com
Phone: 520-481-7093
Toll Free: 866-481-7093
Address: 4315 E. Kestrel Ave. Ste. 140, Tucson, AZ 85733

THINGS I WANT TO PROMOTE (if there is room):
1. Our Website - www.brightlanesites.com

2. Social Media
Twitter: @brightlanesites
Facebook: www.facebook.com/brightlanesites

3. Our Services
Web Design
Internet Marketing
Website Management

```html
<!DOCTYPE html>
<html lang="en">
<head>
<meta charset="utf-8">
<title>Bright Lane Sites – Business Card</title>
<link rel="stylesheet" href="https://fonts.googleapis.com/css2?family=Open+Sans:wght@400;600&display=swap">
<style>
  :root {
    --page-bg: #ffffff;
    --card-top: #ffffff;
    --card-bottom: #e9e9e9;
    --card-edge: #dcdcdc;
    --text-dark: #3a3a3a;
    --title-grey: #555555;
    --accent-orange: #e07a2c;
    --brand-blue: #1b75bb;
    --divider: #c9c9c9;
  }
  html, body {
    margin: 0;
    padding: 0;
    width: 1200px;
    height: 705px;
    overflow: hidden;
    background: var(--page-bg);
    font-family: "Open Sans", Arial, sans-serif;
  }
  .card {
    position: absolute;
    left: 10px;
    top: 10px;
    width: 1180px;
    height: 686px;
    border-radius: 34px;
    border: 2px solid var(--card-edge);
    box-sizing: border-box;
    overflow: hidden;
    background: linear-gradient(160deg, var(--card-top) 0%, #f7f7f7 45%, var(--card-bottom) 100%);
  }
  .card-swoosh {
    position: absolute;
    inset: 0;
    width: 100%;
    height: 100%;
  }
  .brand {
    position: absolute;
    left: 84px;
    top: 138px;
    display: flex;
    align-items: center;
    gap: 22px;
  }
  .brand-dot {
    width: 72px;
    height: 72px;
    border-radius: 50%;
    background: var(--accent-orange);
  }
  .brand-name {
    font-weight: 600;
    font-size: 58px;
    color: var(--brand-blue);
    letter-spacing: -0.5px;
    line-height: 1;
  }
  .contact {
    position: absolute;
    left: 79px;
    top: 282px;
    font-size: 26px;
    color: var(--text-dark);
    line-height: 43px;
  }
  .contact-row {
    display: grid;
    grid-template-columns: 127px 29px auto;
    margin-bottom: 21px;
  }
  .divider {
    position: absolute;
    left: 722px;
    top: 293px;
    width: 2px;
    height: 271px;
    background: var(--divider);
  }
  .person {
    position: absolute;
    left: 724px;
    width: 466px;
    top: 386px;
    text-align: center;
  }
  .person-name {
    font-size: 67px;
    color: var(--accent-orange);
    line-height: 1;
    margin: 0;
    font-weight: 400;
  }
  .person-title {
    font-size: 46px;
    color: var(--title-grey);
    margin: 34px 0 0;
    line-height: 1;
  }
</style>
</head>
<body>
  <div class="card">
    <svg class="card-swoosh" viewBox="0 0 1180 686" aria-hidden="true">
      <path d="M0 560 C 300 470, 700 700, 1180 520 L1180 686 L0 686 Z" fill="#ffffff" opacity="0.55"/>
      <path d="M640 0 C 820 160, 1000 120, 1180 60 L1180 0 Z" fill="#ffffff" opacity="0.6"/>
    </svg>

    <div class="brand">
      <span class="brand-dot"></span>
      <span class="brand-name">Bright Lane Sites</span>
    </div>

    <div class="contact">
      <div class="contact-row">
        <span>Address</span><span>:</span>
        <span>4315 E. Kestrel Ave. Ste. 140,<br>Tucson, AZ 85733</span>
      </div>
      <div class="contact-row">
        <span>Phone</span><span>:</span><span>520-481-7093</span>
      </div>
      <div class="contact-row">
        <span>Toll Free</span><span>:</span><span>866-481-7093</span>
      </div>
      <div class="contact-row">
        <span>E-mail</span><span>:</span><span>mark@brightlanesites.com</span>
      </div>
    </div>

    <div class="divider"></div>

    <div class="person">
      <h1 class="person-name">Mark Pellow</h1>
      <p class="person-title">President/CEO</p>
    </div>
  </div>
</body>
</html>
```